"Word Cloud" lists of countries, by decade, who have adopted women's suffrage

The winning designer will (eventually, but not necessarily within this project--see "Nice to Haves", below) design a total of eight images, based on the eight lists of countries (see attached files) in order, by decade, that they adopted women's suffrage.

One of the the attached images is a screen shot of five pages of the book KITE: Notes Toward a Borderless Tomorrow, showing how these lists are presently arranged on 6"x9" pages.

We essentially want to spice up these 8 lists and make them more fun to look at, for the reader.

Target Market(s)

General audience. People who want to make a difference. People who want to do something to change the world, and want to read a book about how we can actually do it.

Industry/Entity Type

Political

Font styles to use
Serif
Sans Serif
Decorative
Script

Requirements
Must have
• At least two initial designs, one for each of the two largest lists (lists 5 and 6). All country names must be spelled correctly. A WORD doc has been provided with all the text you need to work with. An EXAMPLE word cloud has been provided for inspiration. The look and feel of these "Country Clouds" wants to go all over the place, but all names should be (at least somewhat) readable.
• IMPORTANT ELEMENTS: (1) There are a few places where current countries were just one, when they got women's suffrage. Keep this info intact, together, in the cloud. EXAMPLE (from list 6):
•  British Leeward Islands (remove ", including today’s:", but keep together with)
•  Antigua and Barbuda
•  British Virgin Islands
•  Montserrat
•  Saint Kitts and Nevis
•  Anguilla
• (2) The names of the countries should stay in roughly the same order as found in the lists, but laid out (very) roughly right to left and then top to bottom, loosely akin to the standard flow of text written in the latin alphabet. It is fine to alter this standard in minor ways to achieve a better look to the design. Just don't move a country found at the top of one list into the middle of that list or down to the bottom, etc.
• These country clouds will be printed in black and white, so keep the designs greyscale.
• These "country clouds" should be 4.5" in width.The largest country clouds, with the most countries found in them, should not exceed 6" in length.
Nice to have
• (Eventually) all 8 lists in the form of "Country Clouds"---that are playful, but with serious elements. Pull up a list of countries by population, have the 20 biggest use the biggest font sizes. Use many different fonts, mix it up! Essentially, these 8 lists all want to become word clouds, with each nation's full name as its own "word." See example cloud.
• Though having all 8 lists in clouds at the end of this project is "nice to have," the winner for this design might simply produce 2 such clouds, along with a cost estimate attached to the submitted design for what they would charge to complete the other 6 clouds.
Should not have
• Do NOT include the textual transitions found between the lists, in the screen shot or word doc. They are there just to help you see how the different graphics will be used and what will go either before or after them.
• No need to use bullet points.

```html
<!DOCTYPE html>
<html lang="en">
<head>
<meta charset="utf-8">
<title>Country Cloud</title>
<link rel="stylesheet" href="https://fonts.googleapis.com/css2?family=Alfa+Slab+One&family=Anton&family=Archivo+Black&family=Arvo:wght@700&family=Boogaloo&family=Chewy&family=Cinzel:wght@400;700&family=Comfortaa:wght@500&family=Cormorant+Garamond&family=Dancing+Script:wght@600&family=Delius&family=Josefin+Sans:wght@600&family=Kaushan+Script&family=Lato:wght@300;400&family=Libre+Baskerville&family=Lobster&family=Lobster+Two:ital,wght@1,700&family=Marcellus&family=Montserrat:wght@400;500&family=Nunito:wght@300;900&family=Open+Sans:ital,wght@0,400;0,700;1,400&family=Oswald:wght@700&family=Patrick+Hand&family=Questrial&family=Quicksand:wght@600&family=Raleway&family=Roboto+Condensed:wght@700&family=Sniglet:wght@800&family=Uncial+Antiqua&family=Yellowtail&display=swap">
<style>
  :root {
    --paper: #ffffff;
    --ink: #2b2b2b;
    --ink-soft: #3a3a3a;
    --ink-grey: #7a7a7a;
  }
  * { margin: 0; padding: 0; box-sizing: border-box; }
  html, body { width: 800px; height: 1200px; overflow: hidden; background: var(--paper); }
  .country-cloud { position: relative; width: 800px; height: 1200px; color: var(--ink); }
  .country { position: absolute; line-height: 1; white-space: nowrap; }
  .up { writing-mode: vertical-rl; transform: rotate(180deg); }
  .down { writing-mode: vertical-rl; }

  .barbados { left: 96px; top: 268px; font: 54px "Yellowtail", "Kaushan Script", cursive; }
  .antigua { left: 147px; top: 332px; font: italic 400 15px "Open Sans", sans-serif; letter-spacing: 1.5px; }
  .bvi { left: 180px; top: 366px; font: 14px "Lato", sans-serif; }
  .montserrat { left: 368px; top: 292px; font: 500 19px "Montserrat", sans-serif; letter-spacing: 2px; }
  .kitts { left: 392px; top: 318px; font: 17px/1.55 "Lobster", cursive; text-align: center; }
  .anguilla { left: 378px; top: 380px; font: 15px "Cinzel", serif; letter-spacing: 3px; }
  .leeward { left: 522px; top: 284px; font: 40px/0.93 "Boogaloo", sans-serif; }
  .windward { left: 112px; top: 402px; font: 40px "Marcellus", serif; line-height: 1.05; }
  .windward span { display: block; }
  .windward .mid { font-size: 29px; letter-spacing: 1px; }
  .windward .last { font-size: 41px; }
  .grenada { left: 332px; top: 409px; font: italic 400 21px "Open Sans", sans-serif; }
  .dominica { left: 303px; top: 438px; font: 26px "Kaushan Script", cursive; }
  .vincent { left: 313px; top: 479px; font: 15px/1.65 "Delius", sans-serif; text-align: center; }
  .lucia { left: 464px; top: 412px; font: 700 19px "Roboto Condensed", sans-serif; letter-spacing: 1px; }
  .guyana { left: 500px; top: 432px; font: 28px "Kaushan Script", cursive; transform: rotate(-20deg); }
  .nepal { left: 508px; top: 500px; font: 46px "Anton", sans-serif; }
  .belize { left: 636px; top: 428px; font: 30px "Chewy", "Sniglet", cursive; letter-spacing: 2px; }
  .columbia { left: 114px; top: 546px; font: 600 44px "Quicksand", sans-serif; letter-spacing: 4px; }
  .libya { left: 186px; top: 544px; font: 800 40px "Sniglet", sans-serif; transform: rotate(-5deg); }
  .lebanon { left: 339px; top: 545px; font: 21px "Questrial", sans-serif; letter-spacing: 2.5px; }
  .ivoire { left: 352px; top: 578px; font: 500 31px "Comfortaa", sans-serif; letter-spacing: 4px; }
  .mexico { left: 192px; top: 620px; font: 700 68px "Oswald", sans-serif; letter-spacing: 2px; color: var(--ink-soft); }
  .peru { left: 452px; top: 618px; font: 38px "Kaushan Script", cursive; }
  .benin { left: 580px; top: 618px; font: 20px "Montserrat", sans-serif; letter-spacing: 1.5px; }
  .ethiopia { left: 508px; top: 654px; font: 27px/1.3 "Patrick Hand", cursive; text-align: center; }
  .ghana { left: 188px; top: 704px; font: 22px "Alfa Slab One", serif; letter-spacing: 1px; }
  .nicaragua { left: 314px; top: 714px; font: 700 19px "Open Sans", sans-serif; }
  .comoros { left: 180px; top: 750px; font: 300 30px "Lato", sans-serif; }
  .cambodia { left: 347px; top: 750px; font: 900 29px "Nunito", sans-serif; color: var(--ink-grey); }
  .bhutan { left: 550px; top: 736px; font: 30px "Lobster", cursive; transform: rotate(-20deg); }
  .mali { left: 611px; top: 772px; font: 31px "Open Sans", sans-serif; }
  .gabon { left: 196px; top: 800px; font: italic 700 19px "Lobster Two", cursive; }
  .honduras { left: 293px; top: 800px; font: 700 27px "Arvo", serif; letter-spacing: 2px; }
  .cayman { left: 118px; top: 852px; font: 300 24px/1.3 "Nunito", sans-serif; text-align: center; }
  .tunisia { left: 230px; top: 842px; font: 30px "Archivo Black", sans-serif; letter-spacing: 1px; }
  .egypt { left: 276px; top: 842px; font: 62px "Libre Baskerville", serif; }
  .mauritius { left: 540px; top: 836px; font: italic 700 30px "Lobster Two", cursive; }
  .somalia { left: 562px; top: 884px; font: 600 25px "Dancing Script", "Kaushan Script", cursive; }
  .burkina { left: 354px; top: 908px; font: 22px "Lato", sans-serif; letter-spacing: 0.5px; }
  .chad { left: 134px; top: 926px; font: 19px "Uncial Antiqua", "Cinzel", serif; }
  .laos { left: 292px; top: 930px; font: 19px "Lato", sans-serif; }
  .brunei { left: 116px; top: 956px; font: 28px "Cormorant Garamond", serif; }
  .madagascar { left: 276px; top: 962px; font: 700 14px "Cinzel", serif; letter-spacing: 0.5px; }
  .tanzania { left: 292px; top: 982px; font: 14px "Lato", sans-serif; }
  .guinea { left: 416px; top: 952px; font: 27px "Yellowtail", "Kaushan Script", cursive; }
  .malaysia { left: 534px; top: 942px; font: 600 30px "Josefin Sans", sans-serif; letter-spacing: 1px; }
  .sanmarino { left: 522px; top: 982px; font: 20px "Raleway", sans-serif; letter-spacing: 2px; }
</style>
</head>
<body>
<main class="country-cloud" aria-label="Countries that adopted women's suffrage in the decade">
  <span class="country barbados">Barbados</span>
  <span class="country antigua">Antigua and Barbuda</span>
  <span class="country bvi">British Virgin Islands</span>
  <span class="country montserrat">Montserrat</span>
  <span class="country kitts">Saint Kitts<br>and Nevis</span>
  <span class="country anguilla">ANGUILLA</span>
  <span class="country leeward">BRITISH<br>LEEWARD<br>ISLANDS</span>

  <span class="country windward"><span>BRITISH</span><span class="mid">WINDWARD</span><span class="last">ISLANDS</span></span>
  <span class="country grenada">Grenada</span>
  <span class="country dominica">Dominica</span>
  <span class="country vincent">st. vincent and<br>the grenadines</span>
  <span class="country lucia up">ST. LUCIA</span>
  <span class="country guyana">Guyana</span>
  <span class="country nepal">NEPAL</span>
  <span class="country belize down">BELIZE</span>

  <span class="country columbia up">COLUMBIA</span>
  <span class="country libya">Libya</span>
  <span class="country lebanon">LEBANON</span>
  <span class="country ivoire">côte d'ivoire</span>
  <span class="country mexico">MEXICO</span>
  <span class="country peru up">Peru</span>
  <span class="country benin">BENIN</span>
  <span class="country ethiopia">ETHIOPIA<br>AND ERITREA</span>
  <span class="country ghana">GHANA</span>
  <span class="country nicaragua">Nicaragua</span>
  <span class="country comoros">Comoros</span>
  <span class="country cambodia">Cambodia</span>
  <span class="country bhutan">Bhutan</span>
  <span class="country mali">Mali</span>
  <span class="country gabon">Gabon</span>
  <span class="country honduras">HONDURAS</span>

  <span class="country cayman">Cayman<br>Islands</span>
  <span class="country tunisia up">TUNISIA</span>
  <span class="country egypt">EGYPT</span>
  <span class="country mauritius">Mauritius</span>
  <span class="country somalia">Somalia</span>
  <span class="country burkina">Burkina Faso</span>
  <span class="country chad">Chad</span>
  <span class="country laos">Laos</span>
  <span class="country brunei">Brunei</span>
  <span class="country madagascar">Madagascar</span>
  <span class="country tanzania">Tanzania</span>
  <span class="country guinea">Guinea</span>
  <span class="country malaysia">MALAYSIA</span>
  <span class="country sanmarino">SAN MARINO</span>
</main>
</body>
</html>
```